5 facebook (and instagram) posts for advertising a service of Online Medicine.
This is NOT a facebook page design. This is just facebook (and Instagram) posts design.

We are a medical company providing medicine at distance, using standard videoconsultation and sometimes videoconsultation with a medical device that collects vital signs.

Each post should have:
- Our logo (attached) – if needed it can be just the circular form, but that´s up to you to decide. Ofcourse some design work can be done to this form (watermark, change in dimension, etc)
- Some posts can have the photo of the device (not all the posts because we also provide videoconsultations without the device) – for this please use our website to collect images (https://www.casaorvalhoverde.com/en/kordalix). You can also use the video of the device to collect images (provided as attachment).
- Some stock image at your decision or collected from our website (https://www.casaorvalhoverde.com/pt/medicina-online) or from the provided video (all of these are licensed and you can use them freely – for instance you can collect doctors from our video)
- One or more of the following headlines (please use different headlines for different posts):
 Revolução na Qualidade da Videoconsulta
 O seu Médico com acesso à informação da sua Orrin Wellbook
 Sincronização com Orrin Wellbook
 Possibilidade de usar o dispositivo Kordalix | Medição à Distância de 6 Sinais Vitais
 Revolução na Saúde
 Revolução na Medicina à Distância
 Um Novo Mundo na Saúde
 Segurança e Fiabilidade na Medicina à Distância
 Excelência na Medicina à Distância
 Baixa Médica Online
 Atestados de Saúde
 Renovação de Receituário
 Planos de Monitorização Remota e Acompanhamento Médico desde 10 EUR / Mês

We need 5 posts, all different between each other but where we can feel an aesthetical and graphic/design continuity/coherence of course.
Each post should be provided on adequate format for facebook and Instagram publishing.

Target Market(s)

Patients

Industry/Entity Type

Medicine

Requirements
Must have
• Check description
Nice to have
• Check description

```html
<!DOCTYPE html>
<html lang="pt">
<head>
<meta charset="utf-8">
<title>Casa Orvalho Verde — Posts</title>
<link rel="stylesheet" href="https://fonts.googleapis.com/css2?family=Inter:wght@400;500;700;800&display=swap">
<style>
  :root{
    --page:#ffffff;
    --post-bg:#ececec;
    --post-bg-2:#e3e7eb;
    --blue:#1497c8;
    --blue-mid:#0f86b8;
    --blue-deep:#0b6f9d;
    --ink:#3a3a3a;
    --ink-soft:#4a4a4a;
    --white:#ffffff;
  }
  *{margin:0;padding:0;box-sizing:border-box}
  html,body{width:1200px;height:2184px;overflow:hidden;background:var(--page);font-family:"Inter",Arial,sans-serif}
  .canvas{position:relative;width:1200px;height:2184px}
  .post{position:absolute;left:135px;width:931px;height:930px;overflow:hidden;box-shadow:0 22px 26px -18px rgba(0,0,0,.25)}
  .post--excelencia{top:91px;background:var(--post-bg)}
  .post--revolucao{top:1117px;background:linear-gradient(160deg,#e9ecef 0%,var(--post-bg-2) 60%,#d9dee3 100%)}
  .post__art{position:absolute;inset:0;width:931px;height:930px}
  .brand{position:absolute;left:44px;top:52px;display:flex;align-items:center;gap:14px}
  .brand__dot{width:66px;height:66px;border-radius:50%;background:var(--blue);flex:none}
  .brand__name{font-weight:800;font-size:26px;line-height:27px;color:var(--blue);text-transform:uppercase;letter-spacing:0;white-space:nowrap}
  .brand__tagline{font-weight:400;font-size:16.5px;color:var(--ink-soft);margin-top:5px;white-space:nowrap}
  .headline{position:absolute;font-weight:700;color:var(--ink);letter-spacing:-1.2px}
  .headline--center{left:0;right:0;top:164px;text-align:center;font-size:60px;line-height:72px}
  .headline--left{left:480px;top:425px;font-size:58px;line-height:72px}
  .footer-text{position:absolute;color:var(--white);font-size:17.5px;line-height:23px;letter-spacing:-.3px}
  .footer-text--address{left:45px;top:826px;font-weight:700}
  .footer-text--contact{left:592px;top:824px;font-weight:400}
  .footer-text--contact b{font-weight:700}
</style>
</head>
<body>
<div class="canvas">

  <section class="post post--excelencia">
    <svg class="post__art" viewBox="0 0 931 930">
      <line x1="372" y1="68" x2="931" y2="68" stroke="var(--blue)" stroke-width="3"/>
      <circle cx="553" cy="68" r="18" fill="none" stroke="var(--blue)" stroke-width="3"/>
      <circle cx="553" cy="68" r="10" fill="var(--blue)"/>
      <line x1="37" y1="183" x2="37" y2="520" stroke="var(--blue)" stroke-width="3"/>
      <circle cx="37" cy="263" r="11" fill="var(--blue)"/>
      <path d="M0 547 C60 480 180 455 290 462 L600 560 C720 600 850 580 931 510 L931 930 L0 930Z" fill="var(--blue-mid)"/>
      <path d="M490 930 C510 850 600 800 720 790 C820 780 880 760 931 730 L931 930Z" fill="var(--blue-deep)"/>
      <circle cx="432" cy="565" r="220" fill="none" stroke="var(--blue)" stroke-width="3"/>
      <circle cx="432" cy="565" r="196" fill="var(--white)"/>
      <g class="icon-orbit" fill="var(--blue)" stroke="var(--white)" stroke-width="3">
        <circle cx="327" cy="371" r="32"/>
        <circle cx="255" cy="425" r="27"/>
        <circle cx="220" cy="498" r="23"/>
        <circle cx="211" cy="566" r="18"/>
        <circle cx="218" cy="623" r="15"/>
        <circle cx="242" cy="681" r="13"/>
      </g>
      <rect x="309" y="365" width="36" height="13" rx="6.5" fill="var(--white)"/>
      <rect x="245" y="417" width="20" height="16" rx="3" fill="var(--white)"/>
      <rect x="213" y="488" width="14" height="20" rx="2" fill="var(--white)"/>
      <rect x="209" y="556" width="4" height="20" fill="var(--white)"/>
      <circle cx="218" cy="623" r="5" fill="var(--white)"/>
      <circle cx="242" cy="681" r="4" fill="var(--white)"/>
      <g role="img" aria-label="Photo of the handheld vital-signs device with touchscreen and ECG pads">
        <rect x="265" y="434" width="500" height="280" rx="140" transform="rotate(8 515 574)" fill="#e4e6e8"/>
        <rect x="285" y="450" width="460" height="248" rx="124" transform="rotate(8 515 574)" fill="#141414"/>
      </g>
    </svg>

    <div class="brand">
      <span class="brand__dot"></span>
      <div>
        <div class="brand__name">Casa Orvalho<br>Verde</div>
        <div class="brand__tagline">Professor Doutor Rui Tavares Lemos</div>
      </div>
    </div>

    <h1 class="headline headline--center">Excelência na<br>Medicina à Distância</h1>

    <p class="footer-text footer-text--address">R. Joaquim Serôdio, nº 14 - 3º Dto<br>1600-210 Lisboa, Portugal</p>
    <p class="footer-text footer-text--contact"><b>T</b> +351 210 000 482<br><b>M</b> info@casaorvalhoverde.com<br><b>URL</b> www.casaorvalhoverde.com</p>
  </section>

  <section class="post post--revolucao">
    <svg class="post__art" viewBox="0 0 931 930">
      <defs>
        <linearGradient id="hexFill" x1="0" y1="0" x2="1" y2="1">
          <stop offset="0" stop-color="#18a3d3"/>
          <stop offset="1" stop-color="#0b76a6"/>
        </linearGradient>
        <linearGradient id="waveFill" x1="0" y1="0" x2="1" y2="0">
          <stop offset="0" stop-color="#1392c4"/>
          <stop offset="1" stop-color="#0a6c9a"/>
        </linearGradient>
        <linearGradient id="portraitFill" x1="0" y1="0" x2="0" y2="1">
          <stop offset="0" stop-color="#c9cdd1"/>
          <stop offset="0.3" stop-color="#f2f2f2"/>
          <stop offset="1" stop-color="#e6e8ea"/>
        </linearGradient>
      </defs>
      <line x1="356" y1="0" x2="396" y2="35" stroke="var(--blue)" stroke-width="9"/>
      <line x1="392" y1="0" x2="450" y2="51" stroke="var(--blue)" stroke-width="9"/>
      <g class="hex-cluster" fill="url(#hexFill)" stroke="var(--post-bg-2)" stroke-width="4">
        <polygon points="923,55 895,103 839,103 811,55 839,7 895,7"/>
        <polygon points="834,106 806,154 750,154 722,106 750,58 806,58"/>
        <polygon points="923,158 895,206 839,206 811,158 839,110 895,110"/>
        <polygon points="112,252 92,287 52,287 32,252 52,217 92,217"/>
        <polygon points="169,300 149,335 109,335 89,300 109,265 149,265"/>
        <polygon points="98,328 78,363 38,363 18,328 38,293 78,293"/>
      </g>
      <g role="img" aria-label="Photo of a smiling doctor in a white coat with a stethoscope">
        <path d="M21 758 L40 480 C60 430 150 400 200 390 L220 170 C260 150 340 160 360 200 L350 390 C410 410 450 440 450 500 L450 758Z" fill="url(#portraitFill)"/>
      </g>
      <g role="img" aria-label="Photo of the handheld vital-signs device with touchscreen and ECG pads">
        <rect x="472" y="188" width="380" height="220" rx="110" transform="rotate(8 662 298)" fill="#e4e6e8"/>
        <rect x="488" y="200" width="348" height="196" rx="98" transform="rotate(8 662 298)" fill="#141414"/>
      </g>
      <path d="M0 655 C130 720 300 770 420 755 C560 740 640 640 760 650 C840 656 900 680 931 700 L931 930 L0 930Z" fill="url(#waveFill)"/>
      <path d="M0 745 C200 810 400 820 600 800 C750 785 850 840 931 815 L931 930 L0 930Z" fill="var(--blue)" opacity=".6"/>
    </svg>

    <div class="brand">
      <span class="brand__dot"></span>
      <div>
        <div class="brand__name">Casa Orvalho<br>Verde</div>
        <div class="brand__tagline">Professor Doutor Rui Tavares Lemos</div>
      </div>
    </div>

    <h1 class="headline headline--left">Revolução na<br>Medicina à<br>Distância</h1>

    <p class="footer-text footer-text--address">R. Joaquim Serôdio, nº 14 - 3º Dto<br>1600-210 Lisboa, Portugal</p>
    <p class="footer-text footer-text--contact"><b>T</b> +351 210 000 482<br><b>M</b> info@casaorvalhoverde.com<br><b>URL</b> www.casaorvalhoverde.com</p>
  </section>

</div>
</body>
</html>
```